【新商品の発売に合わせて商品に貼るラベルデザイン希望】
ターゲット:20代〜50代の女性/美と健康・ダイエットに興味ある人
キャッチコピー:「食べる程キレイになる究極の菌活スイーツ♡」
商品名:ミモリ花雪ジェラート/ドリンク
(デザインはどちらか一つでOK)
商品の特徴:甘酒や豆乳を使い完全無添加・無糖の甘くて美味しい、でも太るどころか食べる程に究極の菌活生活ができてキレイになるスイーツです。
※写真のスイーツのフローズンの部分だけをアイスにしてカップに入れます。
※ドリンクはそのフローズンが液体になっていて、透明のパックに入っています。
それらに貼るラベルのデザインをお願いします。
イメージ:キレイカッコいいか、京都の抹茶の商品を想像するようなシンプルで素朴な感じもOKです。

期待しています。宜しくお願い致します。

ターゲットの女性がそのラベルを見ただけでワクワクするもの。もしくは素朴感とか体に良いと言うのがイメージできるデザインを希望します。
【注記事項】
すみません、依頼したいのはロゴではなく、ラベル全体のデザインです。
勿論ロゴを入れて頂いてもいいですが、欲しいのはそのままラベルとして使えるデザインです。
質問がありましたので・・・

【甘酒のラベルのサイズです】
横7cm×縦12cm なのですが、これを上から被せるようにして折り曲げます。

前から見ると 7cm×7cmのラベル
裏面をみると、横7cm×縦5cm にちょっとした説明文や材料・製造元などを記載します。
ロゴではなく、背景も入れたそのままで使えるラベルを希望します。
裏面は背景だけでOK。

【アイス】
ルヴェロッサ位のサイズです。蓋だけでなく全体のデザインをお願いします。

どちらか出来れば、文字だけをかえてしようしますので、どちらでもOKです!

上手く記載出来てなくて申し訳ありません。
宜しくお願い致します。

珍しかったのと、素朴なイメージが気に入りました。
ありがとうございました

```html
<!DOCTYPE html>
<html lang="ja">
<head>
<meta charset="utf-8">
<title>ミモリ花雪ジェラート ドリンク ラベル</title>
<link href="https://fonts.googleapis.com/css2?family=Shippori+Mincho:wght@500;700;800&family=Noto+Sans+JP:wght@500;700&display=swap" rel="stylesheet">
<style>
  :root{
    --paper:#ffffff;
    --page:#ffffff;
    --rule:#b9b9b9;
    --ink:#4f4f4f;
    --ink-soft:#6a6a6a;
    --pink-bg:#f8d6e5;
    --pink-mid:#f4c6da;
    --blue-tone:#bfe3f3;
    --heart:#e6336b;
    --stamp:#d9588c;
  }
  *{margin:0;padding:0;box-sizing:border-box}
  html,body{width:703px;height:1200px;overflow:hidden;background:var(--page)}
  body{position:relative;font-family:"Shippori Mincho",serif;color:var(--ink)}
  .size-note{position:absolute;left:10px;top:6px;font:500 22px/1 "Noto Sans JP",sans-serif;color:#333}
  .label{position:absolute;left:7px;top:40px;width:691px;height:1150px;border:2px solid var(--rule);background:var(--paper);overflow:hidden}
  .back-panel{position:absolute;left:0;top:0;width:100%;height:560px;background:var(--paper)}
  .front-panel{position:absolute;left:0;top:560px;width:100%;height:588px;
    background:radial-gradient(circle at 22% 35%,var(--blue-tone) 0,transparent 34%),
               radial-gradient(circle at 80% 60%,var(--blue-tone) 0,transparent 32%),
               radial-gradient(circle at 50% 95%,var(--blue-tone) 0,transparent 28%),
               linear-gradient(160deg,var(--pink-bg),var(--pink-mid))}
  .claim{position:absolute;top:34px;left:0;width:100%;text-align:center;font:700 24px/1 "Noto Sans JP",sans-serif;color:#333;letter-spacing:2px;white-space:nowrap}
  .emblem{position:absolute;left:184px;top:116px;width:320px;height:370px}
  .hexagon{position:absolute;left:0;top:0;width:320px;height:370px}
  .brand{position:absolute;left:52px;top:72px;font-weight:800;font-size:30px;line-height:1;letter-spacing:1px;white-space:nowrap}
  .catch{position:absolute;left:52px;top:112px;font-weight:700;font-size:14px;line-height:1.35;color:var(--ink-soft);border-left:2px solid var(--ink-soft);padding-left:7px;white-space:nowrap}
  .catch .hearts{color:var(--heart)}
  .name-sub{position:absolute;left:0;width:100%;top:162px;text-align:center;font-weight:800;font-size:40px;line-height:1;letter-spacing:2px;white-space:nowrap}
  .name-main{position:absolute;left:0;width:100%;top:218px;text-align:center;font-weight:800;font-size:60px;line-height:1;letter-spacing:4px;white-space:nowrap}
  .stamp{position:absolute;left:34px;top:288px;width:70px;height:70px;border:3px solid var(--stamp);border-radius:50%;background:var(--paper);display:flex;align-items:center;justify-content:center;font-weight:800;font-size:24px;line-height:1;color:var(--stamp);white-space:nowrap}
  .en-name{position:absolute;bottom:30px;left:0;width:100%;text-align:center;font-weight:700;font-size:20px;letter-spacing:1px;color:var(--ink);white-space:nowrap}
</style>
</head>
<body>
  <p class="size-note">70mm×120mm</p>
  <div class="label">
    <div class="back-panel"></div>
    <div class="front-panel" role="img" aria-label="淡いピンク地に水色の水玉と白い小花が散るパターン">
      <p class="claim">完全無添加・無糖</p>
      <div class="emblem">
        <svg class="hexagon" viewBox="0 0 320 370" aria-hidden="true">
          <polygon points="160,0 320,92.5 320,277.5 160,370 0,277.5 0,92.5" fill="#ffffff"/>
        </svg>
        <p class="brand">ミモリ花雪</p>
        <p class="catch">食べる程キレイ<span class="hearts">♥♥♥</span>になる<br>究極の菌活スイーツ</p>
        <p class="name-sub">ジェラート</p>
        <p class="name-main">ドリンク</p>
        <div class="stamp">花雪</div>
      </div>
      <p class="en-name">HANAYUKI GELATO DRINK</p>
    </div>
  </div>
</body>
</html>
```